Maple Lantern Kids - pictora Photospot

We are looking for an pictora type wal for our pediatric dental office. We are thinking it could be weaved into a whole bunch of what we do (i.e. potentially water marked or faded in the background on letterhead, as an pictroa type wall in the practice, as a banner or section of the home page on the website, on rack cards, etc.) I’m thinking it would utilize a nice fun cursive script for the wording "Maple Lantern Kids is the spot for...." and a bunch of different sized “spots” with meaningful words that speak to who we are. That list would include things like:

• Fun
• Smiles
• Laughter
• Caring
• Comfort
• Amazing
• Kids
• Toddlers
• Teens
• Friends
• Family
• Health
• Education
• Cheer
• Positivity
• Exceptional Care

From a color perspective….we could look at a couple of options. We could have one version that has it washed out and in the background (more subliminal). We could have one version that was consistent with the colors in our logo. And we could have one version that popped with more color by utilizing the colors in some of the artwork we use throughout the office (snowboard picture as an example)

Target Market(s)

Appeal to hip families with kids

Industry/Entity Type

Pediatric Dental

Font styles to use
Other font styles liked:
• something modern, hip, playful and fun

Colors
0054AA
0677BA
7BADD7
CADEEF
E8F1F8
0094D4
00A9DD
6FCCEA
C7EBF8
E9F6FB
00AB8E
00BBA5
67D7C9
C6EFE9
E9F9F6

Requirements
Must have
• Use of existing logo and a play on "spots" or polka dots with symbpolic wording. Must appeal to young parents and kiddos (including hip teens)
Should not have
• SHOULDNT BE OVER THE TOP KIDS.

```html
<!DOCTYPE html>
<html lang="en">
<head>
<meta charset="utf-8">
<title>Maple Lantern Kids – Spots</title>
<link rel="stylesheet" href="https://fonts.googleapis.com/css2?family=Great+Vibes&family=Yellowtail&display=swap">
<style>
  :root{
    --navy:#0054AA;
    --ink:#0b4c72;
    --blue:#0677BA;
    --periwinkle:#7BADD7;
    --sky:#0094D4;
    --cyan:#00A9DD;
    --aqua:#6FCCEA;
    --ice:#C7EBF8;
    --emerald:#00AB8E;
    --teal:#00BBA5;
    --mint:#67D7C9;
    --light:#E9F6FB;
    --bg-top:#6dd7cb;
    --bg-bottom:#cadeef;
  }
  *{margin:0;padding:0;box-sizing:border-box}
  html,body{width:675px;height:1200px;overflow:hidden}
  body{background:linear-gradient(180deg,var(--bg-top) 0%,#a6dbe0 55%,var(--bg-bottom) 100%)}
  .poster{position:relative;width:675px;height:1200px}
  .headline{
    position:absolute;left:0;right:0;text-align:center;
    font-family:"Great Vibes",cursive;color:var(--ink);font-weight:400;
  }
  .headline--name{top:60px;font-size:76px;line-height:1}
  .headline--lead{top:180px;font-size:72px;line-height:1}
  .spot{
    position:absolute;left:var(--x);top:var(--y);width:var(--d);height:var(--d);
    transform:translate(-50%,-50%);border-radius:50%;background:var(--c);
    box-shadow:2px 4px 6px rgba(0,40,70,.35);
    display:flex;align-items:center;justify-content:center;text-align:center;
    font-family:"Yellowtail",cursive;color:var(--t,var(--ink));
    font-size:var(--fs,30px);line-height:.95;letter-spacing:-.5px;
  }
  .spot--brand{font-size:36px;line-height:1.05;padding:0 24px}
</style>
</head>
<body>
<main class="poster">
  <h1 class="headline headline--name">Maple Lantern Kids</h1>
  <p class="headline headline--lead">is the spot for....</p>

  <!-- plain dots -->
  <span class="spot" style="--x:170.6px;--y:48.1px;--d:37.5px;--c:var(--ice)"></span>
  <span class="spot" style="--x:96.9px;--y:195px;--d:43.8px;--c:var(--periwinkle)"></span>
  <span class="spot" style="--x:567.5px;--y:211.3px;--d:37.5px;--c:var(--periwinkle)"></span>
  <span class="spot" style="--x:493.8px;--y:362.5px;--d:37.5px;--c:var(--ice)"></span>
  <span class="spot" style="--x:627.5px;--y:424.4px;--d:43.8px;--c:var(--sky)"></span>
  <span class="spot" style="--x:48.8px;--y:461.3px;--d:62.5px;--c:var(--cyan)"></span>
  <span class="spot" style="--x:230px;--y:564.4px;--d:43.8px;--c:var(--ice)"></span>
  <span class="spot" style="--x:55.6px;--y:601.3px;--d:43.8px;--c:var(--navy)"></span>
  <span class="spot" style="--x:561.9px;--y:554.4px;--d:37.5px;--c:var(--periwinkle)"></span>
  <span class="spot" style="--x:206.9px;--y:674.4px;--d:43.8px;--c:var(--sky)"></span>
  <span class="spot" style="--x:588.8px;--y:800.6px;--d:62.5px;--c:var(--navy)"></span>
  <span class="spot" style="--x:376.9px;--y:892.5px;--d:62.5px;--c:var(--aqua)"></span>
  <span class="spot" style="--x:48.8px;--y:937.5px;--d:50px;--c:var(--teal)"></span>
  <span class="spot" style="--x:615.6px;--y:1001.9px;--d:62.5px;--c:var(--aqua)"></span>
  <span class="spot" style="--x:437.5px;--y:1012.5px;--d:43.8px;--c:var(--teal)"></span>
  <span class="spot" style="--x:281.9px;--y:1117.5px;--d:62.5px;--c:var(--teal)"></span>

  <!-- brand spot -->
  <div class="spot spot--brand" style="--x:337.5px;--y:431.3px;--d:244px;--c:var(--navy);--t:var(--ice)">Maple Lantern Kids</div>

  <!-- word spots -->
  <div class="spot" style="--x:109.4px;--y:353.1px;--d:135px;--c:var(--ice);--fs:33px">Toddlers</div>
  <div class="spot" style="--x:579.4px;--y:312.5px;--d:116px;--c:var(--ice);--fs:34px">Health</div>
  <div class="spot" style="--x:551.3px;--y:464.4px;--d:75px;--c:var(--navy);--t:var(--ice);--fs:30px">Fun</div>
  <div class="spot" style="--x:137.5px;--y:535.6px;--d:112.5px;--c:var(--teal);--t:var(--light);--fs:32px">Smiles</div>
  <div class="spot" style="--x:463.8px;--y:593.8px;--d:100px;--c:var(--aqua);--fs:32px">Kids</div>
  <div class="spot" style="--x:298.1px;--y:630px;--d:106px;--c:var(--periwinkle);--fs:32px">Teens</div>
  <div class="spot" style="--x:588.8px;--y:662.5px;--d:125px;--c:var(--periwinkle);--t:var(--navy);--fs:34px">Caring</div>
  <div class="spot" style="--x:93.8px;--y:717.5px;--d:144px;--c:var(--emerald);--t:#fff;--fs:33px">Laughter</div>
  <div class="spot" style="--x:444.4px;--y:731.3px;--d:131px;--c:var(--sky);--t:var(--light);--fs:33px">Friends</div>
  <div class="spot" style="--x:297.5px;--y:793.8px;--d:144px;--c:var(--mint);--fs:33px">Positivity</div>
  <div class="spot" style="--x:156.3px;--y:873.8px;--d:144px;--c:var(--cyan);--t:var(--light);--fs:33px">Amazing</div>
  <div class="spot" style="--x:513.8px;--y:922.5px;--d:159px;--c:var(--teal);--t:var(--light);--fs:34px">Education</div>
  <div class="spot" style="--x:305.6px;--y:984.4px;--d:119px;--c:var(--aqua);--fs:36px">Cheer</div>
  <div class="spot" style="--x:135px;--y:1067.5px;--d:190px;--c:var(--mint);--fs:37px">Exceptional<br>Care</div>
  <div class="spot" style="--x:412.5px;--y:1115.6px;--d:138px;--c:var(--sky);--t:var(--light);--fs:34px">Comfort</div>
  <div class="spot" style="--x:586.3px;--y:1109.4px;--d:119px;--c:var(--emerald);--t:var(--light);--fs:33px">Family</div>
</main>
</body>
</html>
```